Create a Eye Catching Web Design

We need an informative web design that needs to be eye catching and unique. All of the information needs to be on that page - We have a shopfront setup in the next 2 weeks so the website needs to be ready asap. We are selling mainly rehabilitation aids and mobility products.

The website is main purpose is to inform customers about our range of products, address and phone number. This is an interim website until we get an ecommerce website setup. We are not looking for an ecommerce website, just simple, eye-catching and informative. clean, crisp and modern -target age 45-75 yo (men and women)

I have included our logo and brochure designed with our range of product categories.

The website needs to be designed, coded and setup completely as a finished product.

As soon as the website design is chosen, the chosen designer would need to get the website up and running. If the website design is chosen and great, we could use the same designer for the ecommerce build as well.

www.tolvenacare.com
www.tolvenacare.com.au

Reason: I haven't received as many designs but variations from the same designers.

Target Market(s)

45-75

Industry/Entity Type

Health And Wellness

Coding

Coded - Design and coding required

Number of Pages Required

2 page

Font styles to use
Sans Serif

Requirements
Nice to have
• clean design, modern feel - not cluttered - something unique. for the market age

```html
<!DOCTYPE html>
<html lang="en">
<head>
<meta charset="utf-8">
<title>Tolvena Care – Mobility &amp; Rehabilitation Aids</title>
<link href="https://fonts.googleapis.com/css2?family=Open+Sans:ital,wght@0,400;0,600;0,700;1,700&family=Raleway:wght@400;600;700&display=swap" rel="stylesheet">
<style>
:root{
  --teal:#1fb2ad;
  --teal-dark:#13807c;
  --red:#e8505b;
  --ink:#333;
  --muted:#777;
  --dark:#262626;
  --darker:#1b1b1b;
  --light:#f4f4f4;
  --white:#fff;
}
*{box-sizing:border-box;margin:0;padding:0}
html,body{width:1200px;height:5232px;overflow:hidden}
body{font-family:"Open Sans",Arial,sans-serif;color:var(--ink);background:var(--white);font-size:14px}
.heading{font-family:"Raleway",Arial,sans-serif;font-weight:600;text-align:center;font-size:40px;color:var(--ink)}
.heading span{color:var(--teal)}
.rule{width:70px;height:3px;background:var(--teal);margin:10px auto 0}

/* top bar */
.topbar{height:32px;background:var(--teal-dark);display:flex;align-items:center;justify-content:space-between;padding:0 40px;color:#fff;font-size:12px}
.topbar .contact{display:flex;gap:22px}
.topbar .social{display:flex;gap:6px}
.topbar .social i{display:block;width:20px;height:20px;border-radius:2px}

/* header */
.header{height:118px;display:flex;align-items:center;justify-content:space-between;padding:0 40px}
.brand{display:flex;align-items:center;gap:10px;font-family:"Raleway",sans-serif;font-weight:700;font-size:30px;color:var(--red)}
.brand b{display:block;width:26px;height:26px;border-radius:50%;background:var(--red)}
.nav{display:flex;gap:38px;font-size:13px;font-weight:600}
.nav a{color:var(--ink);text-decoration:none;padding-bottom:8px}
.nav a.active{border-bottom:3px solid var(--teal)}

/* hero */
.hero{height:595px;position:relative;background:linear-gradient(160deg,#5d7d4c 0%,#8fa57a 35%,#8d8671 60%,#6a6050 100%)}
.hero .caption{position:absolute;left:360px;top:420px;width:400px;height:70px;border:2px solid #fff;background:rgba(0,0,0,.55);color:#fff;font-family:"Raleway",sans-serif;font-weight:700;font-size:30px;display:flex;align-items:center;justify-content:center;letter-spacing:1px}
.hero .caption span{color:var(--red);margin-left:10px}
.hero .dots{position:absolute;left:0;right:0;top:505px;display:flex;justify-content:center;gap:8px}
.hero .dots i{width:9px;height:9px;border-radius:50%;background:rgba(255,255,255,.6)}
.hero .dots i:first-child{background:#fff}

/* about */
.about{height:765px;padding-top:70px}
.about .sub{text-align:center;font-family:"Raleway",sans-serif;font-weight:700;font-size:24px;color:var(--teal);margin-top:22px}
.about .sub span{color:var(--red)}
.about .intro{width:1080px;margin:24px auto 0;font-size:15px;line-height:24px;color:var(--muted)}
.tabs{display:flex;gap:24px;margin:44px 0 0 110px}
.tabs span{width:160px;height:40px;background:var(--teal);color:#fff;font-size:13px;font-weight:600;display:flex;align-items:center;justify-content:center}
.tabs span.on{background:var(--red)}
.about .row{display:flex;gap:40px;margin:36px 0 0 110px}
.about .photo{width:400px;height:230px;background:linear-gradient(135deg,#c7c8b6,#8aa06f 60%,#b9a584)}
.about .row p{width:560px;font-size:13px;line-height:23px;color:var(--muted)}

/* services */
.services{height:590px;position:relative;background:linear-gradient(120deg,#3a3a3a,#5a5550 50%,#2d2d2d);color:#fff;padding-top:90px}
.services::before{content:"";position:absolute;inset:0;background:rgba(0,0,0,.45)}
.services>*{position:relative}
.services .heading{color:#fff}
.svc-grid{display:grid;grid-template-columns:360px 200px 360px;justify-content:center;row-gap:80px;margin-top:60px}
.svc{display:flex;gap:18px;align-items:flex-start}
.svc.left{text-align:right;grid-column:1}
.svc.right{grid-column:3}
.svc h4{color:var(--red);font-size:14px;font-weight:700;margin-bottom:6px;text-transform:uppercase}
.svc p{font-size:12px;line-height:19px;color:#ddd}
.icons{grid-column:2;grid-row:1 / span 2;display:grid;grid-template-columns:80px 80px;grid-gap:60px 30px;justify-content:center;align-content:center}
.icons span{width:80px;height:80px;border-radius:50%;background:var(--teal);display:flex;align-items:center;justify-content:center}
.icons span:nth-child(even){background:var(--red)}
.icons span:nth-child(3){background:var(--red)}
.icons span:nth-child(4){background:var(--teal)}

/* major products */
.major{height:820px;background:var(--light);padding-top:80px}
.major .grid{display:grid;grid-template-columns:520px 520px;gap:70px 60px;justify-content:center;margin-top:60px}
.prod{display:flex;gap:26px}
.prod .pic{width:230px;height:220px;position:relative;background:linear-gradient(160deg,#d6d6d6,#9a9a9a)}
.prod .tag{position:absolute;left:0;bottom:14px;background:rgba(20,20,20,.85);color:#fff;padding:8px 12px;font-size:12px;font-weight:700;text-transform:uppercase}
.prod .tag small{display:block;font-size:9px;font-weight:400}
.prod h4{color:var(--teal);font-style:italic;font-weight:700;font-size:17px;line-height:22px;text-transform:uppercase;margin-bottom:10px}
.prod p{font-size:12px;line-height:20px;color:var(--muted)}

/* other products */
.other{height:730px;padding-top:80px}
.strip{display:flex;margin-top:50px}
.card{width:240px;border-right:1px solid #eee}
.card .pic{height:300px;background:linear-gradient(170deg,#f0f0f0,#c23a3a 70%,#7a1f1f)}
.card:first-child .pic{background:linear-gradient(170deg,#eee,#9da3a8 60%,#444)}
.card:last-child .pic{background:linear-gradient(170deg,#f5f5f5,#d9dde0 60%,#aab2b8)}
.card .name{height:44px;display:flex;align-items:center;justify-content:center;font-size:12px;font-weight:700;text-transform:uppercase}
.card .bar{display:flex;height:28px;font-size:10px;font-weight:700;color:#fff}
.card .bar span{flex:1;display:flex;align-items:center;justify-content:center;background:var(--red)}
.card .bar span:last-child{background:var(--teal)}
.arrows{display:flex;gap:10px;justify-content:center;margin-top:40px}
.arrows span{width:34px;height:34px;background:#111;display:flex;align-items:center;justify-content:center}

/* opening hours */
.hours{height:565px;position:relative;background:linear-gradient(90deg,#4b4a44 0,#6d7f88 24%,var(--teal) 24%,var(--teal) 76%,#7a7268 76%,#3a3633 100%)}
.hours .panel{position:absolute;left:288px;width:624px;top:0;bottom:0;padding:40px 60px;color:#fff;text-align:center}
.hours h3{font-family:"Raleway",sans-serif;font-size:24px;font-weight:700}
.hours h3 span,.hours h5 span{color:var(--red)}
.hours .lead{font-size:13px;line-height:20px;margin-top:12px}
.hours h5{font-size:16px;font-weight:700;margin-top:26px}
.hours .rule{background:#fff;width:50px;height:2px;margin-top:8px}
.hours table{width:420px;margin:22px auto 0;border-collapse:collapse;font-size:13px;text-align:left}
.hours td{padding:7px 0;border-bottom:1px solid rgba(255,255,255,.25)}
.hours td:last-child{text-align:right}
.hours td i{display:inline-block;width:7px;height:7px;border-radius:50%;background:#fff;margin-right:12px}

/* contact */
.contact{height:450px;background:linear-gradient(100deg,var(--red) 0%,#d4706e 40%,#5fb6ad 75%,var(--teal) 100%);padding:60px 170px 0;color:#fff}
.contact .heading{color:#fff;font-size:32px}
.contact .heading span{color:#fff;font-weight:400}
.form{display:flex;gap:40px;margin-top:40px}
.form .col{flex:1}
.form label{display:block;font-size:11px;margin-bottom:3px}
.form .field{height:30px;background:#fff;color:#999;font-size:12px;padding:7px 10px;margin-bottom:10px}
.form .area{height:110px}
.form .send{height:32px;background:var(--red);color:#fff;font-size:12px;font-weight:700;display:flex;align-items:center;justify-content:center;gap:8px}
.info{margin-top:12px;font-size:12px;line-height:22px}

/* footer */
.footer{height:510px;background:var(--dark);color:#ccc;padding:60px 110px 0;display:grid;grid-template-columns:240px 240px 240px 260px;gap:20px}
.footer h4{font-family:"Raleway",sans-serif;color:#fff;font-size:20px;font-weight:700;margin-bottom:22px}
.footer h4 span{color:var(--red)}
.footer p{font-size:12px;line-height:21px}
.footer ul{list-style:none}
.footer li{font-size:12px;background:#333;padding:6px 12px;margin-bottom:7px;width:200px}
.footer .map{height:150px;background:linear-gradient(135deg,#e8e4da,#cfd8c5 50%,#dfe3e8)}
.bottom{height:57px;background:var(--darker);color:#888;font-size:12px;display:flex;align-items:center;justify-content:center;gap:60px}
</style>
</head>
<body>

<div class="topbar">
  <div class="contact"><span>✉ hello@tolvenacare.com</span><span>☎ 0400 318 265</span></div>
  <div class="social"><i style="background:#3b5998"></i><i style="background:#1da1f2"></i><i style="background:#dd4b39"></i><i style="background:#cb2027"></i></div>
</div>

<header class="header">
  <div class="brand"><b></b>TOLVENA CARE</div>
  <nav class="nav"><a class="active">HOME</a><a>ABOUT US</a><a>PRODUCTS</a><a>CONTACT US</a></nav>
</header>

<section class="hero" role="img" aria-label="Photo of two older people riding mobility scooters along a tree-lined path">
  <div class="caption">MOBILITY <span>TO FREEDOM</span></div>
  <div class="dots"><i></i><i></i><i></i><i></i></div>
</section>

<section class="about">
  <h2 class="heading">ABOUT <span>US</span></h2>
  <div class="rule"></div>
  <p class="sub">WELCOME TO <span>TOLVENA CARE</span></p>
  <p class="intro">Our main purpose is to inform customers about our range of products, address and phone number. This is an interim website until we get an ecommerce website setup. We are not looking for an ecommerce website, just simple, eye-catching and informative, clean, crisp and modern, target age 45-75 (men and women).</p>
  <div class="tabs"><span class="on">Our Vision</span><span>Supplies</span><span>Products</span><span>Health Care</span><span>Remedies</span></div>
  <div class="row">
    <div class="photo" role="img" aria-label="Photo of an older couple riding bicycles in a park"></div>
    <p>Our vision is to provide all the facilities including mobility products to our customers. We are leaders in supplying the best quality aids and every product is chosen with care, so you can move freely and safely through your day. We carry massage recliners, daily health care products, electric scooters, walking aids, wound care products, and consumer health products. Visit our shopfront and our friendly team will help you find the right product for your home and lifestyle.</p>
  </div>
</section>

<section class="services" role="img" aria-label="Dark photo of an older man using a wheelchair behind the services">
  <h2 class="heading">OUR <span>SERVICES</span></h2>
  <div class="svc-grid">
    <div class="svc left"><div><h4>Electric Scooters</h4><p>Get freedom back with our range of electric scooters, easy to ride, comfortable and built for daily trips.</p></div></div>
    <div class="icons">
      <span><svg width="40" height="40" viewBox="0 0 40 40" fill="none" stroke="#fff" stroke-width="3"><circle cx="12" cy="30" r="5"/><circle cx="30" cy="30" r="5"/><path d="M12 30h18M24 30V10h6"/></svg></span>
      <span><svg width="40" height="40" viewBox="0 0 40 40" fill="none" stroke="#fff" stroke-width="3"><path d="M20 4v32M12 12h16"/></svg></span>
      <span><svg width="40" height="40" viewBox="0 0 40 40" fill="none" stroke="#fff" stroke-width="3"><rect x="6" y="10" width="28" height="22" rx="3"/><path d="M20 15v12M14 21h12"/></svg></span>
      <span><svg width="40" height="40" viewBox="0 0 40 40" fill="none" stroke="#fff" stroke-width="3"><circle cx="18" cy="26" r="9"/><path d="M18 6v12h12l4 10"/></svg></span>
    </div>
    <div class="svc right"><div><h4>Walking Aids</h4><p>Walkers, frames and walking sticks that give you stable, safe support both indoors and out.</p></div></div>
    <div class="svc left"><div><h4>Wound Care Products</h4><p>Dressings, bandages and skin care items to help healing at home, selected with local nurses.</p></div></div>
    <div class="svc right"><div><h4>Wheelchairs</h4><p>Light, folding and fully adjustable wheelchairs for everyday comfort and easy transport.</p></div></div>
  </div>
</section>

<section class="major">
  <h2 class="heading">MAJOR <span>PRODUCTS</span></h2>
  <div class="rule"></div>
  <div class="grid">
    <div class="prod">
      <div class="pic" role="img" aria-label="Photo of a black massage recliner"><div class="tag">Massage Recliners<small>Available</small></div></div>
      <div><h4>Best Massage<br>Recliners</h4><p>Best massage recliners are available at a very good cost so don't miss your chance and grab your massage recliner from our store today for the best relaxation you can ever get.</p></div>
    </div>
    <div class="prod">
      <div class="pic" role="img" aria-label="Photo of a silver electric mobility scooter"><div class="tag">Electric Scooters<small>Available</small></div></div>
      <div><h4>Best Electric<br>Scooters</h4><p>Best electric scooters are available at a very good cost so don't miss your chance and grab your electric scooter from our store today for the best freedom you can ever get.</p></div>
    </div>
    <div class="prod">
      <div class="pic" role="img" aria-label="Photo of a shower commode chair"><div class="tag">Shower/Commode<br>Chairs<small>Available</small></div></div>
      <div><h4>Best<br>Shower/Commode<br>Chairs</h4><p>Best shower and commode chairs are available at a very good cost so don't miss your chance and grab your chair from our store today for the best support you can ever get.</p></div>
    </div>
    <div class="prod">
      <div class="pic" role="img" aria-label="Photo of a folding wheelchair"><div class="tag">Wheel Chairs<small>Available</small></div></div>
      <div><h4>Best Wheel Chairs</h4><p>Best wheel chairs are available at a very good cost so don't miss your chance and grab your wheel chair from our store today for the best comfort you can ever get.</p></div>
    </div>
  </div>
</section>

<section class="other">
  <h2 class="heading">OTHER <span>PRODUCTS</span></h2>
  <div class="strip">
    <div class="card"><div class="pic" role="img" aria-label="Photo of an electric scooter"></div><div class="name">Electric Scooters</div><div class="bar"><span>MOBILITY</span><span>TOLVENA</span></div></div>
    <div class="card"><div class="pic" role="img" aria-label="Photo of a red and white massage recliner"></div><div class="name">Massage Recliner</div><div class="bar"><span>MOBILITY</span><span>TOLVENA</span></div></div>
    <div class="card"><div class="pic" role="img" aria-label="Photo of a red massage recliner"></div><div class="name">Massage Recliner</div><div class="bar"><span>MOBILITY</span><span>TOLVENA</span></div></div>
    <div class="card"><div class="pic" role="img" aria-label="Photo of a red and black massage recliner"></div><div class="name">Massage Recliner</div><div class="bar"><span>MOBILITY</span><span>TOLVENA</span></div></div>
    <div class="card"><div class="pic" role="img" aria-label="Photo of a blood pressure monitor"></div><div class="name">Blood Pressure Monitor</div><div class="bar"><span>HEALTH</span><span>TOLVENA</span></div></div>
  </div>
  <div class="arrows">
    <span><svg width="12" height="14" viewBox="0 0 12 14"><path d="M10 1 2 7l8 6z" fill="#fff"/></svg></span>
    <span><svg width="12" height="14" viewBox="0 0 12 14"><path d="M2 1l8 6-8 6z" fill="#fff"/></svg></span>
  </div>
</section>

<section class="hours" role="img" aria-label="Photos of an older man with a walker on the left and a woman exercising on the right">
  <div class="panel">
    <h3>OPENING HOURS OF <span>TOLVENA CARE</span></h3>
    <p class="lead">We have chosen the best timings for the ease of our customers so they can easily visit our shop, so they can buy the best mobility products according to their requirements as we are here to help.</p>
    <h5>OPENING <span>HOURS</span></h5>
    <div class="rule"></div>
    <table>
      <tr><td><i></i>Monday</td><td>10:00 am – 5:00 pm</td></tr>
      <tr><td><i></i>Tuesday</td><td>10:00 am – 5:00 pm</td></tr>
      <tr><td><i></i>Wednesday</td><td>10:00 am – 5:00 pm</td></tr>
      <tr><td><i></i>Thursday</td><td>10:00 am – 5:00 pm</td></tr>
      <tr><td><i></i>Friday</td><td>10:00 am – 5:00 pm</td></tr>
      <tr><td><i></i>Saturday</td><td>10:00 am – 2:00 pm</td></tr>
      <tr><td><i></i>Sunday</td><td>Closed</td></tr>
    </table>
  </div>
</section>

<section class="contact">
  <h2 class="heading">Get in <span>Touch with us</span></h2>
  <div class="form">
    <div class="col">
      <label>Your Name</label><div class="field">Enter Name</div>
      <label>Email Address</label><div class="field">Enter Email id</div>
      <label>Mobile No</label><div class="field">Enter mobile no.</div>
      <div class="info">☗ Address: 14 Marlow Street, Kelwood NSW<br>☎ Phone Number: 0400 318 265<br>✉ Email Address: hello@tolvenacare.com</div>
    </div>
    <div class="col">
      <label>Message</label><div class="field area">Enter Your Message</div>
      <div class="send">➤ SEND MESSAGE</div>
    </div>
  </div>
</section>

<footer class="footer">
  <div><h4>ABOUT <span>TOLVENA</span></h4><p>Our main purpose is to inform customers about our range of products, address and phone number. This is an interim website until we get an ecommerce website up.</p><p style="margin-top:14px">We are not looking for an ecommerce website, just simple, eye-catching and informative, clean and modern for our visitors.</p></div>
  <div><h4>OUR <span>PRODUCTS</span></h4><ul><li>Massage Recliners</li><li>Electric Scooters</li><li>Walking Aids</li><li>Everyday Living Aids</li><li>Consumer Health</li><li>Wound Care Products</li></ul></div>
  <div><h4>CONTACT <span>US</span></h4><p>Address:<br>14 Marlow Street,<br>Kelwood NSW<br>Telephone: 0400 318 265<br>hello@tolvenacare.com<br>www.tolvenacare.com.au</p></div>
  <div><h4>OUR <span>LOCATION</span></h4><div class="map" role="img" aria-label="Street map showing the shop location"></div></div>
</footer>

<div class="bottom"><span>© 2017 Tolvena Care</span><span>All rights reserved</span></div>

</body>
</html>
```